Website incl. html for real estate project

We need the design and implementation of a website for a real estate project. Condominiums are built, which are sold.
We upload the sales brochure. The website should be based on the design of the sales brochure.
There are three houses with 5 apartments each. It should be rendered like this. The structure of the menu should be roughly as follows. Most information about the content is either in the appendix as a picture or in the brochure (PDF)):
Home (page 4-5 from the brochure)
House A
house B
house c
overview
basement
Municipal elections (page 6-7 in the brochure pdf)
Contact
Please use Roboto Regular as font.
And one page should give an overview of all apartments with the prices, the living space, etc. as on the file overview2.jpg.
If you go to the House A, House B, or House C menus, a page should come up with the details for that house only. The pages in the brochure are:
House A (Page 10-11)
House B (page 22-23)
House C (page 34-35)
The individual apartments should each be shown on a property page. There the plan / floor plan of the apartment and the pictures from the inside should be shown. As with the object page.jpg attachment.
Für die Designer... Mehr Zeit...
Coded - Design and coding required
1 page

```html
<!DOCTYPE html>
<html lang="en">
<head>
<meta charset="utf-8">
<title>Residential Park at the Maple</title>
<link rel="stylesheet" href="https://fonts.googleapis.com/css2?family=Roboto:wght@400;500;700&family=Roboto+Slab:wght@400;500&display=swap">
<style>
:root{
  --blue:#0b5b86;
  --red:#d71920;
  --orange:#e8893a;
  --ink:#222;
  --text:#444;
  --contact:#1d2b36;
  --footer:#141414;
  --white:#fff;
}
*{box-sizing:border-box;margin:0;padding:0}
html,body{width:1200px;height:4030px;overflow:hidden}
body{position:relative;font-family:"Roboto",sans-serif;color:var(--text);background:var(--white)}
.abs{position:absolute}
.topbar{left:0;top:0;width:1200px;height:24px;background:var(--blue);color:var(--white);font-size:10px}
.topbar .social{left:128px;top:6px;display:flex;gap:13px}
.topbar .social span{width:11px;height:11px;border-radius:50%;background:var(--white);display:block}
.topbar .contact-line{right:127px;top:5px;display:flex;gap:22px}
.nav{left:0;top:24px;width:1200px;height:67px;background:var(--white)}
.brand{display:flex;align-items:center;gap:8px;font-weight:500;letter-spacing:1px;color:var(--blue)}
.brand i{width:12px;height:12px;background:var(--red);display:block}
.nav .brand{left:141px;top:22px;font-size:19px}
.menu{right:130px;top:28px;display:flex;gap:29px;font-size:10px;color:var(--ink);list-style:none}
.menu .active{color:var(--blue)}
.hero{left:0;top:91px;width:1200px;height:475px;clip-path:polygon(0 0,100% 0,100% 81%,0 96%);
  background:linear-gradient(180deg,#5f6a70 0%,#4b5357 45%,#3e4a3a 75%,#38402f 100%)}
.hero-photo{left:0;top:0;width:100%;height:100%}
.hero .veil{inset:0;background:rgba(0,0,0,.35)}
.house-tag{color:var(--white);font-weight:700;font-size:16px;text-align:center}
.house-tag::after{content:"";display:block;width:1px;height:52px;background:var(--white);margin:6px auto 0}
.hero h1{left:0;width:1200px;top:188px;text-align:center;color:var(--white);font-size:36px;font-weight:700;letter-spacing:.5px}
.hero .lead{left:0;width:1200px;top:236px;text-align:center;color:var(--white);font-family:"Roboto Slab",serif;font-size:17px}
.btn-explore{left:541px;top:278px;width:118px;height:35px;background:var(--orange);color:var(--white);font-size:10px;font-weight:500;display:flex;align-items:center;justify-content:center}
.arrow{top:215px}
.btn{display:flex;align-items:center;justify-content:center;background:var(--blue);color:var(--white);font-size:10px;font-weight:500;width:118px;height:35px}
.intro h2{left:130px;top:666px;font-size:32px;font-weight:500;color:var(--ink);line-height:42px}
.body-text{font-size:12.3px;line-height:19.5px;color:var(--text)}
.intro .body-text{left:130px;top:772px;width:480px}
.intro .body-text p+p{margin-top:10px}
.intro-photo{left:656px;top:637px;width:416px;height:388px;border-radius:50%;background:linear-gradient(160deg,#6e8fb0 0%,#c9c7bd 35%,#3d9fc4 60%,#4f7f2a 100%)}
.stat{width:141px;height:141px;border-radius:50%;background:var(--white);box-shadow:0 0 0 3px #f2f2f2,0 3px 10px rgba(0,0,0,.25);text-align:center;font-family:"Roboto Slab",serif;font-size:11px;color:var(--ink);line-height:15px;padding-top:30px}
.stat b{display:block;font-family:"Roboto",sans-serif;color:var(--red);font-size:26px;font-weight:500;line-height:30px;margin-bottom:6px}
.band{left:0;width:1200px;height:387px;background:linear-gradient(90deg,#3a3a3a 0%,#262626 40%,#1a1a1a 100%)}
.house-photo{width:461px;height:356px}
.kicker{font-size:19px;font-weight:500}
.house-name{font-size:32px;font-weight:500;color:var(--red)}
.on-dark{color:var(--white)}
.on-dark .body-text{color:#e4e4e4}
.vicinity{left:0;width:1200px;top:2705px;text-align:center;font-size:32px;font-weight:500;color:var(--ink);line-height:40px}
.map{left:257px;top:2801px;width:687px;height:345px}
.contact{left:0;top:3216px;width:1200px;height:357px;background:var(--contact)}
.contact h2{left:0;width:1200px;top:54px;text-align:center;color:var(--white);font-size:32px;font-weight:500}
.contact .sub{left:0;width:1200px;top:100px;text-align:center;color:#dfe4e8;font-size:11px}
.field{border:1px solid #cfd6db;color:#e9eef1;font-family:"Roboto Slab",serif;font-size:10.5px;padding:12px}
.submit{left:606px;top:251px;width:330px;height:42px;background:var(--blue);color:var(--white);font-size:11px;font-weight:700;display:flex;align-items:center;justify-content:center}
.footer{left:0;top:3573px;width:1200px;height:457px;background:var(--footer);color:var(--white)}
.footer .brand{left:130px;top:80px;font-size:19px}
.footer .about{left:130px;top:133px;width:270px;font-size:10.5px;line-height:17px;font-weight:500}
.footer .circles{left:130px;top:186px;display:flex;gap:6px}
.footer .circles span{width:34px;height:34px;border-radius:50%;background:var(--red);display:block}
.col-title{font-size:13px;font-weight:500;color:var(--blue);letter-spacing:.3px}
.links{list-style:none;font-size:10.5px;line-height:24px}
.ci{display:flex;align-items:center;gap:10px;font-size:10.5px;line-height:14px}
.ci .ico{width:30px;height:30px;border-radius:50%;border:1.5px solid var(--red);display:flex;align-items:center;justify-content:center;flex:none}
.news-input{left:878px;top:89px;width:192px;height:31px;background:var(--white);color:#777;font-size:9.5px;padding:10px 9px}
.news-btn{left:878px;top:128px;width:192px;height:31px;background:var(--blue);font-size:10px;font-weight:700;display:flex;align-items:center;justify-content:center}
.copyright{left:0;width:1200px;top:330px;text-align:center;font-size:11px;font-weight:500}
.copyright span{color:var(--orange)}
.rule{left:290px;top:366px;width:620px;height:1px;background:#2e2e2e}
.disclaimer{left:290px;top:376px;width:620px;text-align:center;font-size:8px;line-height:14px;color:#9a9a9a}
</style>
</head>
<body>

<div class="abs topbar">
  <div class="abs social"><span></span><span></span><span></span></div>
  <div class="abs contact-line">
    <span>&#9742; +1 (555) 014 2200</span>
    <span>&#9993; info@talberg-immo.example</span>
  </div>
</div>

<header class="abs nav">
  <div class="abs brand"><i></i>TALBERG</div>
  <ul class="abs menu">
    <li class="active">HOME</li><li>HOUSE A</li><li>HOUSE B</li><li>HOUSE C</li><li>OVERVIEW</li><li>BASEMENT</li><li>MUNICIPAL ELECTIONS</li><li>CONTACT</li>
  </ul>
</header>

<section class="abs hero">
  <div class="abs hero-photo" role="img" aria-label="Rendering of the three condominium houses with gardens and a cyclist on the path"></div>
  <div class="abs veil"></div>
  <div class="abs house-tag" style="left:228px;top:40px">HOUSE A</div>
  <div class="abs house-tag" style="left:655px;top:102px">HOUSE B</div>
  <div class="abs house-tag" style="left:855px;top:86px">HOUSE C</div>
  <h1 class="abs">RESIDENTIAL PARK AT THE MAPLE</h1>
  <p class="abs lead">High Quality and Modern Condominiums</p>
  <div class="abs btn-explore">EXPLORE MORE</div>
  <svg class="abs arrow" style="left:52px" width="26" height="54" viewBox="0 0 26 54"><polyline points="24,2 2,27 24,52" fill="none" stroke="#fff" stroke-width="2"/></svg>
  <svg class="abs arrow" style="left:1122px" width="26" height="54" viewBox="0 0 26 54"><polyline points="2,2 24,27 2,52" fill="none" stroke="#fff" stroke-width="2"/></svg>
</section>

<section class="intro">
  <h2 class="abs">RESIDENTIAL<br>PARK AT THE MAPLE</h2>
  <div class="abs body-text">
    <p>Condominiums are being built between Birkenstrasse andthe Wiesenweg in Oberried near Talheim.The modern and high quality apartments are against the quiet Quartier Sonnmatt and the beautiful view of the green«Rabenkopf» aligned.The apartments are ideally located in Oberried with goodSunbathing and the nearest bus stop is just under 120 metersaway.</p>
    <p>The apartments are on the upper floor with a spaciousBalcony and on the ground floor with a covered patio andown garden.</p>
  </div>
  <div class="abs btn" style="left:130px;top:947px">READ MORE</div>
  <div class="abs intro-photo" role="img" aria-label="Photo of the apartment buildings with a swimming pool and trees"></div>
</section>

<div class="abs stat" style="left:132px;top:1091px"><b>3</b>Building with<br>Individual Housing<br>Offer</div>
<div class="abs stat" style="left:327px;top:1091px"><b>9</b>Different<br>Floor Plan Types</div>
<div class="abs stat" style="left:529px;top:1091px"><b>27</b>Parking Spaces in<br>the Underground<br>car park</div>
<div class="abs stat" style="left:737px;top:1091px"><b>15</b>Comfortable<br>Apartments</div>
<div class="abs stat" style="left:928px;top:1091px"><b>120</b>Meters<br>up to Bus stop</div>

<section class="abs band" style="top:1302px" role="img" aria-label="Dim kitchen interior in the background"></section>
<div class="abs house-photo" style="left:131px;top:1369px;background:linear-gradient(180deg,#bfc9cf 0%,#cfcfcb 45%,#8f9484 80%,#6f8256 100%)" role="img" aria-label="Rendering of House A with terraces and garden loungers"></div>
<div class="abs on-dark" style="left:690px;top:1350px;width:370px">
  <div class="kicker">Residential Park am Ahorn</div>
  <div class="house-name">House A</div>
  <p class="body-text" style="margin-top:14px">The "House A" building has five modern apartments with individual floor plans. All apartments havea spacious outdoor area with a balcony or a covered patio facing south towards the Rabenkopf,the local mountain in Oberried. The living rooms are equipped with large windows, which fill the rooms with sunlightflooded. The building is accessible directly from the underground car park with the lift.</p>
  <div class="btn" style="margin-top:30px">READ MORE</div>
</div>

<div class="abs" style="left:130px;top:1836px;width:430px">
  <div class="kicker" style="color:var(--ink)">Residential Park am Ahorn</div>
  <div class="house-name">House B</div>
  <p class="body-text" style="margin-top:14px">The "House B" building has five modern apartments with individual floor plans. All apartmentshave a spacious balcony or terrace facing south towards the Rabenkopf, Oberrieder's local mountain,aligned. The living rooms are equipped with large windows, giving the rooms bright sunlightflooded. The building is accessible directly from the underground car park with the lift.</p>
  <div class="btn" style="margin-top:30px">READ MORE</div>
</div>
<div class="abs house-photo" style="left:610px;top:1793px;background:linear-gradient(160deg,#8a8f6c 0%,#a7a48f 40%,#7f8a5f 70%,#a4583f 100%)" role="img" aria-label="Aerial rendering of House B among neighbouring houses"></div>

<section class="abs band" style="top:2254px" role="img" aria-label="Dim attic interior in the background"></section>
<div class="abs house-photo" style="left:131px;top:2219px;background:linear-gradient(160deg,#3f6fb0 0%,#7fa0c8 30%,#6a8f3a 55%,#c0472c 80%,#4f7f2a 100%)" role="img" aria-label="Photo of House C, a red building behind trees and a garden path"></div>
<div class="abs on-dark" style="left:690px;top:2310px;width:380px">
  <div class="kicker">Residential Park am Ahorn</div>
  <div class="house-name">House C</div>
  <p class="body-text" style="margin-top:14px">The "House C" building has five modern apartments with individual and spacious layoutsfloor plans. All apartments have a spacious balcony or terrace in the direction of the RabenkopfOberrieder local mountain. The living rooms are equipped with large windows, which fill the rooms with sunlightflooded. The building is accessible directly from the underground car park with the lift.</p>
  <div class="btn" style="margin-top:30px">READ MORE</div>
</div>

<h2 class="abs vicinity">VICINITY<br>RESIDENTIAL PARK AT THE MAPLE</h2>
<div class="abs map" style="background:linear-gradient(135deg,#e6e6e6,#d9dcd3)" role="img" aria-label="Site plan showing Houses A, B and C and the surrounding streets"></div>

<section class="abs contact">
  <h2 class="abs">CONTACT US</h2>
  <p class="abs sub">Sed ut perspiciatis unde omnis iste natus error sit voluptatem</p>
  <div class="abs field" style="left:264px;top:142px;width:331px;height:43px">Name:</div>
  <div class="abs field" style="left:264px;top:197px;width:331px;height:41px">Email:</div>
  <div class="abs field" style="left:264px;top:251px;width:331px;height:42px">Phone:</div>
  <div class="abs field" style="left:606px;top:142px;width:330px;height:96px">Comments:</div>
  <div class="abs submit">SUBMIT</div>
</section>

<footer class="abs footer">
  <div class="abs brand"><i></i>TALBERG</div>
  <p class="abs about">The building is covered with 18 to 30 cm of breathable rock woolisolated.</p>
  <div class="abs circles"><span></span><span></span><span></span></div>

  <div class="abs" style="left:451px;top:55px">
    <div class="col-title">QUICK LINKS</div>
    <ul class="links" style="margin-top:6px">
      <li>Home</li><li>House A</li><li>House B</li><li>House c</li><li>Overview</li><li>Basement</li><li>Municipal elections</li><li>Contact</li>
    </ul>
  </div>

  <div class="abs" style="left:627px;top:55px">
    <div class="col-title">CONTACTS</div>
    <div class="ci" style="margin-top:13px"><span class="ico"><svg width="10" height="13" viewBox="0 0 10 13"><path d="M5 0C2.2 0 0 2.2 0 5c0 3.5 5 8 5 8s5-4.5 5-8C10 2.2 7.8 0 5 0z" fill="#fff"/><circle cx="5" cy="5" r="1.8" fill="#141414"/></svg></span><span>Talberg Immobilien<br>AG Switzerland</span></div>
    <div class="ci" style="margin-top:18px"><span class="ico"><svg width="12" height="12" viewBox="0 0 12 12"><path d="M2.5 0.5l2 2.5-1.2 1.5c.7 1.6 2 2.9 3.7 3.7l1.5-1.2 2.5 2-1.3 2.5C4.5 11 1 7.5.5 1.8z" fill="#fff"/></svg></span><span>+41 00 555 01 23</span></div>
    <div class="ci" style="margin-top:15px"><span class="ico"><svg width="12" height="9" viewBox="0 0 12 9"><rect width="12" height="9" fill="#fff"/><polyline points="0,0 6,5 12,0" fill="none" stroke="#141414" stroke-width="1.2"/></svg></span><span>kontakt@talberg-immo.example</span></div>
  </div>

  <div class="abs col-title" style="left:878px;top:55px">NEWSLETTER</div>
  <div class="abs news-input">Enter Your Email</div>
  <div class="abs news-btn">SUBSCRIBE</div>

  <p class="abs copyright">Copyright © 2022 <span>Talberg</span>. All Rights Reserved.</p>
  <div class="abs rule"></div>
  <p class="abs disclaimer">The sales documents and illustrations shown here serve to inform potential buyers to the best of our knowledge and belief. No legal claims can be derived from this documentation.</p>
</footer>

</body>
</html>
```